KV PowerPoint Design

I need a slick PowerPoint template following my newly designed logo (see the attached ZIP file for logo details, fonts, and colors).
Please also see the Sample.pptx file for an idea of the simplicity and slickness I am after (do not consider the colors or fonts from the Sample file, just as an idea). Other ideas are very welcome.

```html
<!DOCTYPE html>
<html lang="en">
<head>
<meta charset="utf-8">
<title>KV Presentation Template</title>
<link href="https://fonts.googleapis.com/css2?family=Montserrat:wght@300;400;500;700;800&display=swap" rel="stylesheet">
<style>
  :root {
    --backdrop: #c9c9ce;
    --slide: #ffffff;
    --navy: #0d1a80;
    --navy-deep: #002680;
    --royal: #0047a6;
    --sky: #bde0fc;
    --mist: #e4ebfa;
    --slate: #9aa8c4;
  }
  * { box-sizing: border-box; margin: 0; padding: 0; }
  html, body { width: 1200px; height: 1200px; overflow: hidden; }
  body {
    background: var(--backdrop);
    font-family: "Montserrat", sans-serif;
    color: var(--navy);
    position: relative;
  }
  .slide {
    position: absolute;
    left: 241px;
    width: 718px;
    height: 478px;
    background: var(--slide);
    overflow: hidden;
  }
  .slide--cover { top: 109px; }
  .slide--content { top: 612px; }

  .slide__number {
    position: absolute;
    left: 51px;
    font-weight: 800;
    font-size: 68px;
    line-height: 1;
    letter-spacing: -2px;
    color: var(--slate);
  }
  .slide--cover .slide__number { top: 52px; }
  .slide--content .slide__number { top: 52px; }

  .slide__title {
    position: absolute;
    left: 53px;
    font-weight: 700;
    font-size: 30px;
    line-height: 1;
    color: var(--navy);
  }
  .slide--cover .slide__title { top: 132px; }
  .slide--content .slide__title { top: 133px; }

  .slide__subtitle {
    position: absolute;
    left: 54px;
    top: 167px;
    font-weight: 300;
    font-size: 18px;
    color: var(--navy);
  }

  .slide__body {
    position: absolute;
    left: 54px;
    top: 184px;
    width: 370px;
    font-weight: 500;
    font-size: 9.6px;
    line-height: 11.5px;
    color: var(--navy);
  }
  .slide__body p + p { margin-top: 7px; }

  .brand {
    position: absolute;
    display: flex;
    align-items: center;
    gap: 8px;
  }
  .brand__dot {
    border-radius: 50%;
    background: var(--navy);
  }
  .brand__name {
    font-weight: 700;
    color: var(--navy);
    line-height: 1;
  }
  .slide--cover .brand { left: 40px; top: 380px; }
  .slide--cover .brand__dot { width: 44px; height: 44px; }
  .slide--cover .brand__name { font-size: 26px; }
  .slide--content .brand { left: 46px; top: 402px; }
  .slide--content .brand__dot { width: 28px; height: 28px; }
  .slide--content .brand__name { font-size: 17px; }

  .mosaic { position: absolute; top: 0; height: 478px; }
  .slide--cover .mosaic { left: 331px; width: 387px; }
  .slide--content .mosaic { left: 506px; width: 212px; }
  .tile { position: absolute; }

  .fill-navy { background: var(--navy-deep); }
  .fill-royal { background: var(--royal); }
  .fill-sky { background: var(--sky); }
  .fill-mist { background: var(--mist); }
  .fill-haze { background: linear-gradient(180deg, #9aaacc 0%, #8c9fc8 100%); }
  .photo-pale { background: linear-gradient(180deg, #a4b2d2 0%, #c9d2e8 55%, #eef1f9 100%); }
  .photo-blue { background: linear-gradient(180deg, #1c5cd6 0%, #1848b8 45%, #3a86ea 100%); }
  .photo-light { background: linear-gradient(180deg, #4f9cf0 0%, #3f86e0 50%, #2d6fd0 100%); }
</style>
</head>
<body>

<section class="slide slide--cover">
  <div class="slide__number">01</div>
  <h1 class="slide__title">Lorem Ipsum</h1>
  <p class="slide__subtitle">Lorem Ipsum dolor sit</p>
  <div class="brand">
    <span class="brand__dot"></span>
    <span class="brand__name">KV</span>
  </div>
  <div class="mosaic">
    <div class="tile photo-pale" style="left:0;top:0;width:131px;height:386px" role="img" aria-label="Portrait of a smiling woman with dark hair, tinted pale blue"></div>
    <div class="tile fill-navy" style="left:0;top:386px;width:131px;height:92px"></div>
    <div class="tile fill-royal" style="left:131px;top:0;width:135px;height:93px"></div>
    <div class="tile photo-blue" style="left:131px;top:93px;width:135px;height:293px" role="img" aria-label="Portrait of a smiling young woman, tinted blue"></div>
    <div class="tile fill-sky" style="left:131px;top:386px;width:135px;height:92px"></div>
    <div class="tile fill-mist" style="left:266px;top:0;width:121px;height:93px"></div>
    <div class="tile photo-light" style="left:266px;top:93px;width:121px;height:385px" role="img" aria-label="Portrait of a bearded man with glasses in a checked shirt, tinted blue"></div>
  </div>
</section>

<section class="slide slide--content">
  <div class="slide__number">02</div>
  <h2 class="slide__title">Lorem Ipsum</h2>
  <div class="slide__body">
    <p>Lorem ipsum dolor sit amet, consectetur adipiscing elit, sed do eiusmod tempor incididunt ut labore et dolore magna aliqua. Quis ipsum suspendisse ultrices gravida. Risus commodo viverra maecenas accumsan lacus vel facilisis.</p>
    <p>Lorem ipsum dolor sit amet, consectetur adipiscing elit, sed do eiusmod tempor incididunt ut labore et dolore magna aliqua. Quis ipsum suspendisse ultrices gravida. Risus commodo viverra maecenas accumsan lacus vel facilisis.</p>
    <p>Lorem ipsum dolor sit amet, consectetur adipiscing elit, sed do eiusmod tempor incididunt ut labore et dolore magna aliqua. Quis ipsum suspendisse ultrices gravida. Risus commodo viverra maecenas accumsan lacus vel facilisis</p>
  </div>
  <div class="brand">
    <span class="brand__dot"></span>
    <span class="brand__name">KV</span>
  </div>
  <div class="mosaic">
    <div class="tile fill-haze" style="left:0;top:0;width:72px;height:238px"></div>
    <div class="tile photo-pale" style="left:0;top:238px;width:72px;height:190px" role="img" aria-label="Portrait of a smiling woman with dark hair, tinted pale blue"></div>
    <div class="tile fill-navy" style="left:0;top:428px;width:72px;height:50px"></div>
    <div class="tile fill-royal" style="left:72px;top:0;width:74px;height:268px"></div>
    <div class="tile photo-blue" style="left:72px;top:268px;width:74px;height:160px" role="img" aria-label="Portrait of a smiling young woman, tinted blue"></div>
    <div class="tile fill-sky" style="left:72px;top:428px;width:74px;height:50px"></div>
    <div class="tile fill-mist" style="left:146px;top:0;width:66px;height:268px"></div>
    <div class="tile photo-light" style="left:146px;top:268px;width:66px;height:210px" role="img" aria-label="Portrait of a bearded man with glasses in a checked shirt, tinted blue"></div>
  </div>
</section>

</body>
</html>
```